New website for a commercial real estate consulting company

What we’re looking for in a new web site:
• Desktop and mobile friendly
• Clear navigation
• Strong graphics
• Professional appearance
• The ability to update it ourselves
• Site is for information purposes only – no transactions required
• Traffic counts – number of visits per page?
• A firm quote on costs to develop and launch
• SSL
Attached is a copy of the revised text we propose to use, including our new logo. (The pagination can be different than as shown.)
Our current website address is www.brightlanecounselgroup.ca

```html
<!DOCTYPE html>
<html lang="en">
<head>
<meta charset="utf-8">
<title>Brightlane Counsel Group — Our Clients</title>
<link href="https://fonts.googleapis.com/css2?family=Montserrat:wght@500;600;700&family=Work+Sans:wght@400;600;700&display=swap" rel="stylesheet">
<style>
  :root {
    --teal: #12c9c2;
    --white: #ffffff;
    --ink-dark: #161616;
    --quote-grey: #7a7a7a;
    --body-grey: #6a6a6a;
    --footer-text: #d6d6d6;
    --photo-a: #3a4656;
    --photo-b: #8a98a8;
  }
  * { margin: 0; padding: 0; box-sizing: border-box; }
  html, body { width: 1200px; height: 1200px; overflow: hidden; background: var(--white); }
  .page { position: relative; width: 1200px; height: 1200px; }

  .clients { position: absolute; left: 0; top: 0; width: 1200px; height: 534px; background: var(--teal); }
  .clients-title {
    position: absolute; top: 14px; width: 100%; text-align: center;
    font-family: 'Montserrat', sans-serif; font-weight: 700; font-size: 26px; color: var(--white);
  }
  .client-list { list-style: none; position: absolute; left: 83px; top: 78px; }
  .client-item {
    position: relative; padding-left: 38px; height: 39.5px; line-height: 24px;
    font-family: 'Montserrat', sans-serif; font-weight: 600; font-size: 14px;
    letter-spacing: 2px; text-transform: uppercase; color: var(--white);
  }
  .client-item.wrap { height: 79px; line-height: 39.5px; margin-top: -8px; padding-top: 0; }
  .client-item.after-wrap { margin-top: -8px; }
  .client-item .tick { position: absolute; left: 0; top: 0; width: 22px; height: 22px; }
  .client-item.wrap .tick { top: 8px; }
  .teamwork-photo {
    position: absolute; left: 559px; top: 79px; width: 568px; height: 378px;
    background: radial-gradient(ellipse at 45% 50%, #c89880 0%, #8a6a5a 22%, var(--photo-b) 50%, var(--photo-a) 100%);
    box-shadow: 0 4px 10px rgba(0,0,0,0.25);
  }

  .motto {
    position: absolute; top: 700px; width: 100%; display: flex; justify-content: center; align-items: center; gap: 18px;
    font-family: 'Work Sans', sans-serif; font-weight: 700; font-size: 25px; color: var(--quote-grey);
  }
  .motto .mark { font-family: Georgia, serif; font-size: 58px; line-height: 1; height: 40px; margin-top: -8px; }
  .contact-line {
    position: absolute; top: 911px; width: 100%; text-align: center;
    font-family: 'Montserrat', sans-serif; font-weight: 500; font-size: 14px; color: var(--body-grey);
  }

  .site-footer { position: absolute; left: 0; top: 966px; width: 1200px; height: 234px; background: var(--ink-dark); }
  .footer-brand { position: absolute; left: 84px; top: 70px; display: flex; align-items: center; gap: 10px;
    font-family: 'Work Sans', sans-serif; font-weight: 600; font-size: 15px; letter-spacing: 1px; color: var(--white); }
  .footer-brand .brand-square { width: 14px; height: 14px; background: var(--white); }
  .copyright { position: absolute; left: 85px; top: 152px; font-family: 'Work Sans', sans-serif; font-size: 13px; line-height: 21px; color: var(--footer-text); }
  .footer-nav { position: absolute; left: 491px; top: 89px; list-style: none;
    font-family: 'Work Sans', sans-serif; font-size: 13px; line-height: 21px; color: var(--footer-text); }
  .footer-nav .caps { font-size: 10.5px; font-weight: 600; letter-spacing: 1px; text-transform: uppercase; }
  .footer-contact { position: absolute; left: 824px; top: 114px;
    font-family: 'Work Sans', sans-serif; font-size: 13px; line-height: 21px; color: var(--footer-text); }
</style>
</head>
<body>
<div class="page">
  <section class="clients">
    <h2 class="clients-title">Our Clients Include</h2>
    <ul class="client-list">
      <li class="client-item"><svg class="tick" viewBox="0 0 22 22"><polyline points="2,11 8,18 20,2" fill="none" stroke="#fff" stroke-width="3.5" stroke-linecap="round" stroke-linejoin="round"/></svg>Chartered Banks</li>
      <li class="client-item"><svg class="tick" viewBox="0 0 22 22"><polyline points="2,11 8,18 20,2" fill="none" stroke="#fff" stroke-width="3.5" stroke-linecap="round" stroke-linejoin="round"/></svg>Mortgage Bankers</li>
      <li class="client-item"><svg class="tick" viewBox="0 0 22 22"><polyline points="2,11 8,18 20,2" fill="none" stroke="#fff" stroke-width="3.5" stroke-linecap="round" stroke-linejoin="round"/></svg>Public REITs &amp; REOCs</li>
      <li class="client-item"><svg class="tick" viewBox="0 0 22 22"><polyline points="2,11 8,18 20,2" fill="none" stroke="#fff" stroke-width="3.5" stroke-linecap="round" stroke-linejoin="round"/></svg>Private Equity Firms</li>
      <li class="client-item wrap"><svg class="tick" viewBox="0 0 22 22"><polyline points="2,11 8,18 20,2" fill="none" stroke="#fff" stroke-width="3.5" stroke-linecap="round" stroke-linejoin="round"/></svg>Family-Owned Real Estate Investment<br>Companies</li>
      <li class="client-item after-wrap"><svg class="tick" viewBox="0 0 22 22"><polyline points="2,11 8,18 20,2" fill="none" stroke="#fff" stroke-width="3.5" stroke-linecap="round" stroke-linejoin="round"/></svg>Life Insurance Companies</li>
      <li class="client-item"><svg class="tick" viewBox="0 0 22 22"><polyline points="2,11 8,18 20,2" fill="none" stroke="#fff" stroke-width="3.5" stroke-linecap="round" stroke-linejoin="round"/></svg>Pension Funds</li>
      <li class="client-item"><svg class="tick" viewBox="0 0 22 22"><polyline points="2,11 8,18 20,2" fill="none" stroke="#fff" stroke-width="3.5" stroke-linecap="round" stroke-linejoin="round"/></svg>Non-Bank Lenders</li>
      <li class="client-item"><svg class="tick" viewBox="0 0 22 22"><polyline points="2,11 8,18 20,2" fill="none" stroke="#fff" stroke-width="3.5" stroke-linecap="round" stroke-linejoin="round"/></svg>Brokerage Firms</li>
    </ul>
    <div class="teamwork-photo" role="img" aria-label="Photo from above of many hands stacked together in the centre as a team gesture, on a grey floor"></div>
  </section>

  <blockquote class="motto">
    <span class="mark">&ldquo;</span>
    <span class="motto-text">Reputation is the currency of the 21st century</span>
    <span class="mark">&rdquo;</span>
  </blockquote>

  <p class="contact-line">For more information please call us at 905-555-0148, email Nora Whitfield at nora.whitfield@brightlanecounselgroup.ca, or click below.</p>

  <footer class="site-footer">
    <div class="footer-brand"><span class="brand-square"></span>BRIGHTLANE COUNSEL GROUP</div>
    <p class="copyright">© 2019 Brightlane Counsel Group.<br>All rights reserved.</p>
    <ul class="footer-nav">
      <li>Home</li>
      <li>Who We Are</li>
      <li>What We Do</li>
      <li>Contact Us</li>
      <li class="caps">Industry Events Calendar</li>
    </ul>
    <div class="footer-contact">
      nora.whitfield@brightlanecounselgroup.ca<br>905-555-0148
    </div>
  </footer>
</div>
</body>
</html>
```